TEK Logistics - Banner 2.5' x 8' for 20+ locations

Need a banner designed that will pop. This banner will be displayed at over 20 of our transportation facilities. Goal is for the banner to grab the attention of employees, contractors and clients and help reinforce our mission and core values. Designed needs to include TEK Logo, our core values and mission statement. Red and Black are the main company colors and we need to stay within that theme and color pallet. Attached is a previous version that was too basic and boring. Willing to consider a design that excludes the mission statement.

Gathering more feedback

```html
<!DOCTYPE html>
<html lang="en">
<head>
<meta charset="utf-8">
<title>TEK Logistics – Core Values Banner</title>
<link href="https://fonts.googleapis.com/css2?family=Roboto:wght@400;500;700&display=swap" rel="stylesheet">
<style>
  :root{
    --page:#ebebeb;
    --charcoal:#2c2a28;
    --red:#d42729;
    --white:#ffffff;
  }
  *{box-sizing:border-box;margin:0;padding:0}
  html,body{width:1200px;height:1200px;overflow:hidden;background:var(--page)}
  body{position:relative;font-family:"Roboto",Arial,sans-serif;color:var(--white)}
  .banner{position:absolute;left:78px;top:410px;width:1044px;height:327px;background:var(--charcoal);overflow:hidden}
  .decor{position:absolute;left:0;top:0}
  .brand{position:absolute;left:26px;top:152px;width:170px;text-align:center;font-weight:700;font-size:22px;letter-spacing:1px;color:var(--red)}
  .value{position:absolute;width:262px;height:62px;border-radius:20px;background:var(--charcoal);box-shadow:6px 8px 14px rgba(0,0,0,.55)}
  .value .icon{position:absolute;left:14px;top:3px;width:56px;height:56px}
  .value .label{position:absolute;left:81px;top:50%;transform:translateY(-50%);font-size:13.6px;line-height:17px;font-weight:400;text-transform:uppercase}
  .mission{position:absolute;left:260px;width:760px;top:268px;text-align:center;font-size:15.5px;line-height:20px;font-weight:500;text-transform:uppercase}
</style>
</head>
<body>
<main class="banner">
  <svg class="decor" width="1044" height="327" viewBox="0 0 1044 327" aria-hidden="true">
    <circle cx="134" cy="161" r="165" fill="var(--red)"/>
    <circle cx="122" cy="142" r="152" fill="var(--charcoal)"/>
    <circle cx="127" cy="130" r="140" fill="var(--white)"/>
    <circle cx="110" cy="126" r="139" fill="var(--charcoal)"/>
    <polygon points="562,317 1044,317 1044,327 556,327" fill="var(--red)"/>
    <path d="M970 230 A48 48 0 1 1 990 318" fill="none" stroke="var(--red)" stroke-width="6"/>
    <path d="M975 240 A40 40 0 0 1 1020 295" fill="none" stroke="var(--red)" stroke-width="3"/>
  </svg>

  <div class="brand">TEK LOGISTICS</div>

  <div class="value" style="left:351px;top:27px">
    <svg class="icon" viewBox="0 0 56 56" aria-hidden="true"><path d="M28 3 A25 25 0 0 1 28 53" fill="none" stroke="var(--red)" stroke-width="4"/><circle cx="26" cy="28" r="13" fill="none" stroke="#fff" stroke-width="1.6"/><path d="M20 28 l4 4 l8 -8" fill="none" stroke="#fff" stroke-width="1.8"/></svg>
    <p class="label">Do the right things<br>for the right reasons</p>
  </div>
  <div class="value" style="left:351px;top:106px">
    <svg class="icon" viewBox="0 0 56 56" aria-hidden="true"><path d="M28 3 A25 25 0 0 1 28 53" fill="none" stroke="var(--red)" stroke-width="4"/><g fill="none" stroke="#fff" stroke-width="1.5"><rect x="15" y="34" width="4" height="6"/><rect x="21" y="31" width="4" height="9"/><rect x="27" y="28" width="4" height="12"/><rect x="33" y="24" width="4" height="16"/><path d="M14 30 L34 17 M30 16 L35 16 L35 21"/></g></svg>
    <p class="label">Pursue growth<br>and development</p>
  </div>
  <div class="value" style="left:351px;top:185px">
    <svg class="icon" viewBox="0 0 56 56" aria-hidden="true"><path d="M28 3 A25 25 0 0 1 28 53" fill="none" stroke="var(--red)" stroke-width="4"/><g fill="none" stroke="#fff" stroke-width="1.6"><rect x="14" y="22" width="14" height="10" rx="5"/><rect x="24" y="26" width="14" height="10" rx="5"/></g></svg>
    <p class="label">Build a positive<br>team atmosphere</p>
  </div>

  <div class="value" style="left:692px;top:27px">
    <svg class="icon" viewBox="0 0 56 56" aria-hidden="true"><path d="M28 3 A25 25 0 0 1 28 53" fill="none" stroke="var(--red)" stroke-width="4"/><g fill="none" stroke="#fff" stroke-width="1.6"><rect x="22" y="17" width="17" height="18"/><path d="M22 23 H15 L11 29 V35 H22"/><circle cx="16" cy="36" r="2.5"/><circle cx="33" cy="36" r="2.5"/><path d="M26 25 l3 3 l6 -6"/></g></svg>
    <p class="label">Deliver wow<br>through service</p>
  </div>
  <div class="value" style="left:692px;top:106px">
    <svg class="icon" viewBox="0 0 56 56" aria-hidden="true"><path d="M28 3 A25 25 0 0 1 28 53" fill="none" stroke="var(--red)" stroke-width="4"/><g fill="none" stroke="#fff" stroke-width="1.6"><path d="M26 15 L36 19 V28 C36 35 31 39 26 41 C21 39 16 35 16 28 V19 Z"/><path d="M21 28 l4 4 l6 -7"/></g></svg>
    <p class="label">Do everything<br>safely</p>
  </div>
  <div class="value" style="left:692px;top:185px">
    <svg class="icon" viewBox="0 0 56 56" aria-hidden="true"><path d="M28 3 A25 25 0 0 1 28 53" fill="none" stroke="var(--red)" stroke-width="4"/><g fill="none" stroke="#fff" stroke-width="1.6"><circle cx="26" cy="28" r="13"/><path d="M26 20 l2.4 5 5.4.6 -4 3.7 1.1 5.3 -4.9-2.7 -4.9 2.7 1.1-5.3 -4-3.7 5.4-.6z"/></g></svg>
    <p class="label">Have fun</p>
  </div>

  <p class="mission">Provide the best customer experience while creating an environment of growth and opportunity for our customers, employees, and service providers</p>
</main>
</body>
</html>
```